Zanquerra Business Card Design

Zanquerra is a small and new restaurant/ bar location in Hong Kong. The name "Djibouti" derives from an African country. There is no specific reason behind other than the fact, that the bar is somewhat inspired by African elements (only inspired but not purely based on African cuisine etc.).

The bar is somewhat a fusion of African, Mediterranean and Oriental (Old French Vietnam) elements.

However, it is very imperative to stress, that the overall look and feel of Zanquerra is a very high end cocktail lounge/ bar location. The bar is tucked away in a hidden alley, so people will have to know about it. The idea is to send the consumer off in an Escape or hidden remote location where they are at ease in a hip, stylish and trendy environment.

The card needs to feel high-end.

Final logo artwork has been attached and also pictures of the bar/ restaurant itself. The logo ie monkey head cannot be modified. However, the background color and the color of the type "ZANQUERRA" can be changed.

The following details need to fit onto the business card. Of course they can be arranged to your liking:

LOGO

Tobin Le
Partner

+852 90817364
xxx@zanquerra-bar.com
www.zanquerra-bar.com
4C, Pelham Lane, Wan Chai, Hong Kong

Industry/Entity Type

Restaurant

```html
<!DOCTYPE html>
<html lang="en">
<head>
<meta charset="utf-8">
<title>Zanquerra Business Card</title>
<link rel="stylesheet" href="https://fonts.googleapis.com/css2?family=Oswald:wght@500;700&family=Roboto+Slab:wght@800&display=swap">
<style>
  :root {
    --backdrop: #d9d4cc;
    --card-dark: #0c0c0d;
    --card-mid: #232325;
    --accent-red: #c8102e;
    --text-light: #f4f1ee;
    --logo-brown: #5a3a2a;
  }
  * { box-sizing: border-box; margin: 0; padding: 0; }
  html, body { width: 1200px; height: 1000px; overflow: hidden; }
  body {
    background: var(--backdrop);
    display: flex;
    flex-direction: column;
    align-items: center;
    justify-content: center;
    gap: 70px;
  }
  .card {
    position: relative;
    width: 640px;
    height: 366px;
    border-radius: 6px;
    overflow: hidden;
    background: radial-gradient(ellipse at 35% 30%, var(--card-mid), var(--card-dark) 75%);
    box-shadow: 0 10px 24px rgba(0,0,0,0.25);
  }
  .card-texture {
    position: absolute; inset: 0;
    background: linear-gradient(160deg, rgba(255,255,255,0.06), rgba(255,255,255,0) 45%, rgba(0,0,0,0.2));
  }

  /* Front */
  .card-front .brand {
    position: absolute; inset: 0;
    display: flex; flex-direction: column; align-items: center; justify-content: center;
    gap: 26px;
  }
  .brand-mark {
    width: 130px; height: 130px; border-radius: 50%;
    background: var(--logo-brown);
  }
  .brand-name {
    font-family: "Roboto Slab", serif;
    font-weight: 800;
    font-size: 64px;
    letter-spacing: 2px;
    color: var(--text-light);
    line-height: 1;
  }

  /* Back */
  .back-layout {
    position: absolute;
    left: 50%; top: 50%;
    width: 760px;
    transform: translate(-50%, -50%) rotate(-32deg);
    display: flex; flex-direction: column; align-items: center;
  }
  .rule {
    width: 100%; height: 4px;
    background: var(--text-light);
    border-top: 2px solid var(--accent-red);
    border-bottom: 2px solid var(--accent-red);
  }
  .person { text-align: center; margin: 20px 0 14px; }
  .person-name {
    font-family: "Oswald", sans-serif; font-weight: 700;
    font-size: 40px; color: var(--text-light); line-height: 1;
    letter-spacing: 1px;
  }
  .person-role {
    font-family: "Oswald", sans-serif; font-weight: 500;
    font-size: 17px; color: var(--text-light); letter-spacing: 2px;
  }
  .contact-list {
    list-style: none; text-align: center; margin-bottom: 22px;
    font-family: "Oswald", sans-serif; font-weight: 500;
    font-size: 17px; line-height: 1.45; color: var(--text-light);
    letter-spacing: 1px; text-transform: uppercase;
  }
</style>
</head>
<body>
  <section class="card card-front" aria-label="Business card front">
    <div class="card-texture"></div>
    <div class="brand">
      <div class="brand-mark"></div>
      <div class="brand-name">ZANQUERRA</div>
    </div>
  </section>

  <section class="card card-back" aria-label="Business card back">
    <div class="card-texture"></div>
    <div class="back-layout">
      <div class="rule"></div>
      <div class="person">
        <div class="person-name">TOBIN LE</div>
        <div class="person-role">PARTNER</div>
      </div>
      <ul class="contact-list">
        <li>+852 90817364</li>
        <li>xxx@zanquerra-bar.com</li>
        <li>www.zanquerra-bar.com</li>
        <li>4C, Pelham Lane, Wan Chai, Hong Kong</li>
      </ul>
      <div class="rule"></div>
    </div>
  </section>
</body>
</html>
```